Professionell und kommunikativ, kommen gerne wieder.
Zielgruppe
Wir transportieren Güter und Waren aller Art rund um die Welt. Hauptsächlich Luftfracht, aber auch per Schiff und an Land. Hauptsächlich richten wir uns damit an Firmenkunden, weniger an Privatkunden. Für unsere neue Website benötigen wir ein Design.
Aufgabenstellung
Wir benötigen ein Webdesign für den Relaunch unserer Website. Unsere Ideen für unsere neue Website haben wir bereits skizziert (Anlage). Diese Mockups bedürfen nun eines Designs.
Dazu ergänzend gelten die folgenden, formalen Vorgaben:
• 1140px breit, gerne auch Ideen für die Darstellung auf Smartphones und Tablets
• Logo links oben
• Navigation oben waagerecht
• Dropdown-Navigation am Desktop, Hamburger für die mobile Navigation
• Verwendung eines Grid-Systems wie Bootstrap
• Mindestschriftgröße für Mengentext: 16px (bei groß ausfallenden Fonts 15px)
Wir haben keine Hausschriftart und keine festgelegten Farben. Wir möchten aber unser Logo weiterverwenden und da bietet es sich natürlich an, auf dem Rot aufzubauen.

```html
<!DOCTYPE html>
<html lang="en">
<head>
<meta charset="utf-8">
<title>Skyvaro – Air Freight Solutions</title>
<link href="https://fonts.googleapis.com/css2?family=Arimo:wght@400;700&display=swap" rel="stylesheet">
<style>
:root{
  --red:#e30613;
  --navy:#0c3663;
  --ink:#1e1e1e;
  --muted:#8a8a8a;
  --light:#f3f3f3;
  --line:#e4e4e4;
  --footer:#1c1c1c;
  --white:#ffffff;
  --rating:#4a7fd4;
}
*{box-sizing:border-box;margin:0;padding:0}
html,body{width:1200px;height:4068px;overflow:hidden}
body{font-family:"Arimo",Arial,sans-serif;color:var(--ink);background:var(--white);position:relative}
.abs{position:absolute}
.topbar{top:0;left:0;width:1200px;height:32px;font-size:9px;letter-spacing:.5px;color:#555}
.topbar span{position:absolute;top:10px}
.nav{top:32px;left:0;width:1200px;height:52px;border-bottom:1px solid var(--line)}
.brand{font-size:24px;letter-spacing:-.5px;color:#666;font-weight:400;white-space:nowrap}
.brand-dot{display:inline-block;width:14px;height:14px;border-radius:50%;background:var(--red);margin-left:4px;vertical-align:middle}
.nav-link{top:20px;font-size:9px;font-weight:700;letter-spacing:.6px;color:#333}
.nav-cta{top:0;left:906px;width:106px;height:52px;background:var(--red);color:#fff;font-size:9px;font-weight:700;letter-spacing:.8px;display:flex;align-items:center;justify-content:center}
.hero{top:84px;left:0;width:1200px;height:469px;background:linear-gradient(180deg,#6e6e6a 0%,#4d4c48 55%,#3a3632 100%)}
.hero h1{position:absolute;left:188px;top:158px;color:#fff;font-size:46px;line-height:48px;font-weight:400;letter-spacing:-.5px}
.hero h1 b{font-weight:700}
.hero p{position:absolute;left:188px;top:270px;width:450px;color:#eee;font-size:11.5px;line-height:16px}
.btn{position:absolute;display:flex;align-items:center;justify-content:center;font-size:10px;font-weight:700;letter-spacing:1.8px}
.btn-red{background:var(--red);color:#fff}
.btn-ghost{border:1.5px solid #fff;color:#fff}
.side-tab{left:1143px;width:57px;height:56px;background:var(--red);color:#fff;font-size:7px;font-weight:700;display:flex;flex-direction:column;align-items:center;justify-content:center;gap:4px}
.eyebrow{font-size:9px;font-weight:700;color:#222;display:flex;align-items:center;gap:8px}
.eyebrow::before{content:"";width:24px;height:2px;background:var(--red)}
.eyebrow em{font-style:normal;font-weight:400;color:var(--muted);margin-left:-5px}
.h2{font-size:33px;font-weight:700;line-height:36px;letter-spacing:-.3px}
.body-s{font-size:9.5px;line-height:13px;color:#666}
.card{background:var(--light)}
.card h3{font-size:13px;line-height:18px;font-weight:400}
.card h3 b{font-weight:700}
.icon-badge{width:20px;height:20px;background:var(--red);display:flex;align-items:center;justify-content:center}
.reach{top:1622px;left:0;width:1200px;height:394px}
.philo{top:2016px;left:0;width:1200px;height:654px;background:var(--light)}
.pcard{background:#fff;padding:36px 26px 0 26px}
.pcard h4{font-size:13px;font-weight:700;margin:12px 0 10px}
.faq-item{width:403px;height:57px;background:var(--light);display:flex;align-items:center;justify-content:space-between;padding:0 22px 0 20px;font-size:11.5px;font-weight:700;line-height:15px;color:#333}
.faq-item span:last-child{color:var(--red);font-size:14px;font-weight:400}
.partner{top:3390px;height:58px;display:flex;align-items:center;font-size:17px;font-weight:700;color:#333;white-space:nowrap}
.partner-sep{top:3390px;width:1px;height:58px;background:var(--line)}
.footer{top:3562px;left:0;width:1200px;height:506px;background:var(--footer);color:#fff}
.fhead{font-size:8.5px;font-weight:700;letter-spacing:1.8px}
.flink{font-size:8.5px;color:#ddd;display:flex;gap:6px}
.flink::before{content:"›";color:var(--red)}
</style>
</head>
<body>

<div class="abs topbar">
  <span style="left:188px">+49 30 5550 1200 <span style="position:static;color:#999">– CALL US ANYTIME</span></span>
  <span style="right:188px;font-weight:700">INFO@SKYVARO-FREIGHT.COM</span>
</div>

<header class="abs nav">
  <div class="abs brand" style="left:188px;top:11px">SKYVARO<span class="brand-dot"></span></div>
  <span class="abs nav-link" style="left:689px">SERVICES ⌄</span>
  <span class="abs nav-link" style="left:771px">ABOUT US</span>
  <span class="abs nav-link" style="left:840px">CONTACT</span>
  <div class="abs nav-cta">GET A QUOTE</div>
</header>

<section class="abs hero" role="img" aria-label="Photo of a large cargo aircraft parked on an airfield under a cloudy sky, being loaded">
  <h1>Swift and Reliable<br><b>Air Freight Solutions</b></h1>
  <p>Experience the speed and efficiency of our air freight services. With a global network, advanced tracking systems, and a dedicated team, we ensure your cargo reaches its destination quickly and securely. Trust us for seamless logistics solutions that keep your business soaring.</p>
  <div class="btn btn-red" style="left:188px;top:368px;width:118px;height:36px">GET A QUOTE</div>
  <div class="btn btn-ghost" style="left:319px;top:368px;width:127px;height:36px">OUR SERVICES</div>
</section>
<div class="abs side-tab" style="top:303px">
  <svg width="16" height="16" viewBox="0 0 16 16" fill="none" stroke="#fff" stroke-width="1.2"><rect x="3" y="1.5" width="10" height="13"/><path d="M5.5 5h5M5.5 8h5M5.5 11h3"/></svg>GET A QUOTE</div>
<div class="abs side-tab" style="top:362px">
  <svg width="16" height="16" viewBox="0 0 16 16" fill="none" stroke="#fff" stroke-width="1.2"><path d="M4 2l2.5 3-1.5 1.5c.8 1.8 2.2 3.2 4 4L10.5 9l3 2.5-1.5 2C7 13.5 2.5 9 2.5 3.5z"/></svg>CONTACT</div>

<div class="abs eyebrow" style="left:188px;top:744px">WHO <em>WE ARE</em></div>
<h2 class="abs h2" style="left:188px;top:764px;width:320px">Skyvaro - Your Air Freight Expert</h2>
<p class="abs" style="left:188px;top:858px;width:300px;font-size:12px;line-height:16px;color:#222">Skyvaro is a dedicated team of logistics experts, providing exceptional sea freight solutions worldwide.</p>
<p class="abs body-s" style="left:188px;top:921px;width:300px">With a customer-centric approach, we prioritize transparency, communication, and personalized support.</p>
<p class="abs body-s" style="left:188px;top:960px;width:310px">Trust us to handle your cargo needs with care and professionalism.</p>
<div class="abs" role="img" aria-label="Photo of a passenger jet taking off from a runway at sunset" style="left:557px;top:714px;width:453px;height:289px;background:linear-gradient(160deg,#7fa9c9 0%,#c9a6b0 40%,#8fa6b8 70%,#4a5866 100%)"></div>
<div class="abs" style="left:592px;top:955px;width:163px;height:92px;background:#fff;box-shadow:0 4px 14px rgba(0,0,0,.15)">
  <div class="abs" style="left:22px;top:18px;font-size:36px;font-weight:700;line-height:36px;color:var(--rating)">4.7</div>
  <svg class="abs" style="left:14px;top:62px" width="80" height="14" viewBox="0 0 70 14"><g fill="#f4b400"><path id="st" d="M7 0l2 4.5 5 .5-3.8 3.3 1.1 5L7 10.8 2.7 13.3l1.1-5L0 5l5-.5z"/><use href="#st" x="14"/><use href="#st" x="28"/><use href="#st" x="42"/><use href="#st" x="56"/></g></svg>
  <div class="abs" style="left:100px;top:16px;font-size:11px;color:#333">Rating</div>
  <div class="abs" style="left:100px;top:30px;font-size:6px;color:#999">average rating</div>
  <div class="abs" style="left:110px;top:48px;width:24px;height:24px;border-radius:50%;background:#d9d9d9"></div>
</div>

<div class="abs eyebrow" style="left:188px;top:1160px">OUR <em>SKILLS</em></div>
<h2 class="abs h2" style="left:188px;top:1180px">What we offer</h2>
<svg class="abs" style="left:802px;top:1181px" width="16" height="16" viewBox="0 0 16 16" fill="none" stroke="#999" stroke-width="1.3"><path d="M14 8H2M6 4L2 8l4 4"/></svg>
<span class="abs" style="left:840px;top:1183px;font-size:9px;color:#888">3 / 6</span>
<div class="abs" style="left:872px;top:1175px;width:28px;height:28px;background:#333;display:flex;align-items:center;justify-content:center"><svg width="14" height="14" viewBox="0 0 16 16" fill="none" stroke="#fff" stroke-width="1.5"><path d="M2 8h12M10 4l4 4-4 4"/></svg></div>

<div class="abs card" style="left:188px;top:1249px;width:224px;height:251px">
  <div class="abs" style="left:36px;top:40px;width:40px;height:40px;border-radius:50%;background:#fff"></div>
  <div class="abs icon-badge" style="left:68px;top:26px"><svg width="10" height="10" viewBox="0 0 10 10" fill="none" stroke="#fff" stroke-width="1.3"><path d="M9 5H1M4 2L1 5l3 3"/></svg></div>
  <h3 class="abs" style="left:35px;top:98px;width:170px"><b>Import -</b> Simplify your Air freight imports with Skyvaro.</h3>
  <p class="abs body-s" style="left:35px;top:160px;width:150px">Our expert team handles documentation, customs clearance, and transportation coordination for seamless and efficient import operations.</p>
</div>
<div class="abs card" style="left:431px;top:1249px;width:224px;height:251px">
  <div class="abs" style="left:36px;top:40px;width:40px;height:40px;border-radius:50%;background:#fff"></div>
  <div class="abs icon-badge" style="left:68px;top:26px"><svg width="10" height="10" viewBox="0 0 10 10" fill="none" stroke="#fff" stroke-width="1.3"><path d="M1 5h8M6 2l3 3-3 3"/></svg></div>
  <h3 class="abs" style="left:35px;top:98px;width:160px"><b>Export -</b> Efficient Air Freight Export Services</h3>
  <p class="abs body-s" style="left:35px;top:141px;width:150px">Our expert team handles documentation, customs clearance, and transportation coordination for seamless and efficient import operations.</p>
</div>
<div class="abs card" style="left:675px;top:1249px;width:224px;height:251px">
  <div class="abs" style="left:36px;top:40px;width:40px;height:40px;border-radius:50%;background:#fff"></div>
  <div class="abs icon-badge" style="left:68px;top:26px;border-radius:50%"><svg width="10" height="10" viewBox="0 0 10 10" fill="none" stroke="#fff" stroke-width="1.3"><path d="M2 5l2 2 4-4"/></svg></div>
  <h3 class="abs" style="left:35px;top:98px;width:170px"><b>Warehousing -</b> Secure and Reliable Warehousing Solutions</h3>
  <p class="abs body-s" style="left:35px;top:160px;width:150px">Our expert team handles documentation, customs clearance, and transportation coordination for seamless and efficient import operations.</p>
</div>
<div class="abs card" style="left:918px;top:1249px;width:224px;height:251px">
  <div class="abs" style="left:36px;top:40px;width:40px;height:40px;border-radius:50%;background:#fff"></div>
  <div class="abs icon-badge" style="left:68px;top:26px;border-radius:50%"><svg width="10" height="10" viewBox="0 0 10 10" fill="none" stroke="#fff" stroke-width="1.3"><path d="M2 5l2 2 4-4"/></svg></div>
  <h3 class="abs" style="left:35px;top:98px;width:160px"><b>Support -</b> Secure and Reliable Warehousing</h3>
  <p class="abs body-s" style="left:35px;top:141px;width:150px">Our expert team handles documentation, customs clearance, and transportation coordination for seamless and efficient import operations.</p>
</div>
<div class="abs card" style="left:1161px;top:1249px;width:39px;height:251px"></div>

<section class="abs reach">
  <div class="abs" style="left:0;top:0;width:662px;height:394px;background:var(--navy)"></div>
  <div class="abs" role="img" aria-label="Photo of a jumbo jet flying above a sea of clouds under a blue sky" style="left:662px;top:0;width:538px;height:394px;background:linear-gradient(180deg,#2f64a8 0%,#6d9bd1 50%,#dfe8f2 75%,#b9c7d8 100%)"></div>
  <h2 class="abs h2" style="left:188px;top:74px;color:#fff">Reach Out to Us</h2>
  <p class="abs" style="left:188px;top:122px;width:400px;color:#fff;font-size:15px;line-height:21px;font-weight:700">We're here to assist you. Contact our team for any inquiries or support you may need.</p>
  <div class="btn" style="left:188px;top:207px;width:162px;height:42px;border:1.5px solid #fff;color:#fff">GET A QUOTE</div>
  <svg class="abs" style="left:384px;top:218px" width="22" height="22" viewBox="0 0 16 16" fill="none" stroke="#fff" stroke-width="1"><path d="M4 2l2.5 3-1.5 1.5c.8 1.8 2.2 3.2 4 4L10.5 9l3 2.5-1.5 2C7 13.5 2.5 9 2.5 3.5z"/></svg>
  <span class="abs" style="left:416px;top:220px;color:#fff;font-size:16px;font-weight:700">+49 30 5550 1288</span>
  <svg class="abs" style="left:188px;top:297px" width="14" height="14" viewBox="0 0 14 14" fill="none" stroke="#fff" stroke-width="1"><circle cx="7" cy="7" r="6"/><path d="M7 3.5V7l2.5 1.5"/></svg>
  <div class="abs" style="left:217px;top:294px;font-size:8.5px;color:#fff;font-weight:700">Our business hours:<br><span style="font-weight:400;color:#7fa6d6">Monday to Friday - 8:00 AM to 4:30 PM (CET)</span></div>
  <div class="abs" style="left:414px;top:294px;font-size:8.5px;color:#fff;font-weight:700">We are open in:<br><span style="font-weight:400;color:#7fa6d6">2 hours and 32 minutes.</span></div>
</section>

<section class="abs philo">
  <div class="abs eyebrow" style="left:552px;top:97px">OUR <em>VALUES</em></div>
  <h2 class="abs h2" style="left:0;width:1200px;text-align:center;top:114px">Our Philosophy</h2>
  <div class="abs pcard" style="left:188px;top:199px;width:262px;height:182px">
    <svg width="18" height="18" viewBox="0 0 18 18" fill="none" stroke="var(--red)" stroke-width="1.2"><path d="M9 1.5l2.3 4.8 5.2.6-3.9 3.6 1 5.2L9 13.2l-4.6 2.5 1-5.2L1.5 6.9l5.2-.6z"/></svg>
    <h4>Expertise</h4><p class="body-s">With years of experience in the industry, our team has the knowledge and expertise to handle all your air freight needs efficiently and effectively.</p></div>
  <div class="abs pcard" style="left:469px;top:199px;width:262px;height:182px">
    <svg width="18" height="18" viewBox="0 0 18 18" fill="none" stroke="var(--red)" stroke-width="1.2"><path d="M1.5 5V1.5H5M13 1.5h3.5V5M16.5 13v3.5H13M5 16.5H1.5V13"/><circle cx="9" cy="7" r="2.5"/><path d="M5 14c.5-2.5 2-3.5 4-3.5s3.5 1 4 3.5"/></svg>
    <h4>Customer Focus</h4><p class="body-s">Your satisfaction is our top priority. We provide personalized support, responsive customer service, and transparent communication throughout the entire process.</p></div>
  <div class="abs pcard" style="left:750px;top:199px;width:262px;height:182px">
    <svg width="18" height="18" viewBox="0 0 18 18" fill="none" stroke="var(--red)" stroke-width="1.2"><circle cx="9" cy="9" r="7.5"/><ellipse cx="9" cy="9" rx="3.3" ry="7.5"/><path d="M1.5 9h15M2.7 5h12.6M2.7 13h12.6"/></svg>
    <h4>Global Network</h4><p class="body-s">We have established a vast network of partners and agents worldwide, enabling us to provide seamless door-to-door solutions to any destination.</p></div>
  <div class="abs pcard" style="left:188px;top:400px;width:403px;height:155px">
    <svg width="18" height="18" viewBox="0 0 18 18" fill="none" stroke="var(--red)" stroke-width="1.2"><rect x="1.5" y="1.5" width="4" height="4"/><rect x="12.5" y="12.5" width="4" height="4"/><path d="M5.5 3.5h7v9M5.5 14.5h7M3.5 5.5v9"/></svg>
    <h4>Customization</h4><p class="body-s">We understand that every shipment is unique. That's why we offer tailored solutions, ensuring your cargo is handled with precision and according to your specific requirements.</p></div>
  <div class="abs pcard" style="left:609px;top:400px;width:403px;height:155px">
    <svg width="18" height="18" viewBox="0 0 18 18" fill="none" stroke="var(--red)" stroke-width="1.2"><circle cx="9" cy="9" r="2.8"/><path d="M9 1.5v2.5M9 14v2.5M1.5 9H4M14 9h2.5M3.7 3.7l1.8 1.8M12.5 12.5l1.8 1.8M3.7 14.3l1.8-1.8M12.5 5.5l1.8-1.8"/></svg>
    <h4>Reliability</h4><p class="body-s">We prioritize reliability and on-time delivery. You can trust us to keep your supply chain running smoothly, with proactive communication and real-time tracking.</p></div>
</section>

<div class="abs eyebrow" style="left:546px;top:2765px">FIND <em>ANSWERS</em></div>
<h2 class="abs h2" style="left:0;width:1200px;text-align:center;top:2784px">FAQ</h2>
<div class="abs faq-item" style="left:188px;top:2869px"><span>What is sea freight and how does it work?</span><span>+</span></div>
<div class="abs faq-item" style="left:188px;top:2932px"><span>How long does sea freight shipping typically take?</span><span>+</span></div>
<div class="abs faq-item" style="left:188px;top:2994px"><span>Do you offer both full container load (FCL) and less<br>than container load (LCL) options?</span><span>+</span></div>
<div class="abs faq-item" style="left:188px;top:3057px"><span>Are there any restrictions or prohibited items for sea<br>freight shipping?</span><span>+</span></div>
<div class="abs faq-item" style="left:188px;top:3120px"><span>What happens if there are delays or disruptions in the<br>sea freight transportation?</span><span>+</span></div>
<div class="abs faq-item" style="left:609px;top:2869px"><span>What are the advantages of choosing sea freight over<br>other shipping methods?</span><span>+</span></div>
<div class="abs faq-item" style="left:609px;top:2932px"><span>What are the main factors that affect sea freight<br>shipping costs?</span><span>+</span></div>
<div class="abs faq-item" style="left:609px;top:2994px"><span>What is the process for customs clearance during sea<br>freight shipments?</span><span>+</span></div>
<div class="abs faq-item" style="left:609px;top:3057px"><span>How can I track the progress of my sea freight<br>shipment?</span><span>+</span></div>
<div class="abs faq-item" style="left:609px;top:3120px"><span>What documentation is required for sea freight<br>shipments, and how can I ensure compliance?</span><span>+</span></div>

<div class="abs eyebrow" style="left:188px;top:3295px">WHO <em>TRUST US</em></div>
<h2 class="abs" style="left:188px;top:3315px;font-size:23px;font-weight:700">Our Partners and clients</h2>
<div class="abs partner" style="left:188px">Kestrelwing Air</div>
<div class="abs partner-sep" style="left:357px"></div>
<div class="abs partner" style="left:390px">Harlowby Skylines</div>
<div class="abs partner-sep" style="left:570px"></div>
<div class="abs partner" style="left:598px">Steinmark Motors</div>
<div class="abs partner-sep" style="left:755px"></div>
<div class="abs partner" style="left:788px">Relay Network</div>

<footer class="abs footer">
  <div class="abs brand" style="left:188px;top:80px;color:#bbb">SKYVARO<span class="brand-dot"></span></div>
  <p class="abs" style="left:188px;top:119px;font-size:9px;line-height:14px;font-weight:700">Unlocking Logistics Excellence:<br>Your Reliable Partner</p>
  <div class="abs" style="left:188px;top:200px;width:70px;height:50px;background:#555;border-radius:4px"></div>
  <p class="abs" style="left:188px;top:262px;font-size:9px;font-weight:700">Partner of Global Air Trade Assoc.</p>

  <div class="abs fhead" style="left:399px;top:84px">OUR SERVICES</div>
  <div class="abs flink" style="left:399px;top:114px">AIR FREIGHT</div>
  <div class="abs flink" style="left:399px;top:144px">SEA FREIGHT</div>
  <div class="abs flink" style="left:399px;top:174px">LAND TRANSPORT</div>
  <div class="abs flink" style="left:399px;top:204px">AIRLINE SERVICES</div>

  <div class="abs fhead" style="left:539px;top:84px">LEGAL INFORMATION</div>
  <div class="abs flink" style="left:539px;top:114px">DATA PRIVACY POLICY</div>
  <div class="abs flink" style="left:539px;top:144px">IMPRINT</div>
  <div class="abs fhead" style="left:539px;top:196px">OTHER INFORMATION</div>
  <div class="abs flink" style="left:539px;top:226px">FAQ</div>
  <div class="abs flink" style="left:539px;top:256px">CONTACT</div>

  <div class="abs" style="left:188px;top:310px;width:505px;height:1px;background:#3a3a3a"></div>
  <div class="abs" style="left:188px;top:351px;width:213px;height:74px;background:#fff;display:flex;align-items:center;gap:12px;padding-left:16px">
    <div style="width:34px;height:34px;border-radius:50%;background:#d9d9d9"></div>
    <div><div style="font-size:9px;color:#333">ReviewHub Rating</div>
      <div style="font-size:15px;font-weight:700;color:#e8a400">4.8 ★★★★★</div>
      <div style="font-size:6px;color:#999">See all our reviews</div></div>
  </div>

  <div class="abs" role="img" aria-label="Street map showing the company location with a red pin" style="left:750px;top:81px;width:262px;height:161px;background:linear-gradient(135deg,#eef0ea 0%,#e3e7df 60%,#b9d3ee 100%)"></div>
  <div class="abs fhead" style="left:750px;top:266px;font-size:8px">CONTACT INFORMATION</div>
  <div class="abs" style="left:750px;top:296px;font-size:9px;line-height:16px;color:#ddd"><b style="color:#fff">Skyvaro GmbH</b><br>Lindenring 14<br>10115 Musterstadt<br>Tel.: +49 30 5550 1288<br>E-Mail: <u>info@skyvaro-freight.de</u></div>
  <div class="btn" style="left:750px;top:393px;width:262px;height:32px;border:1.5px solid #fff;color:#fff;font-size:9px">CONTACT FORM</div>
</footer>

</body>
</html>
```